Need Business Cards for my Business

email address: rkpmarlowhollowworks@vendrimail.com
web address: rkpmarlowhollowworks.net
Slogan: We offer various QVN licenses
Rowland K. Pemberly
Please stick with colors of Company Logo
would like the card to be more of the color example of the logo.
If you need PDF copy of logo email me at the above account.
Creative control rests with you.

Industry/Entity Type

Business

Contact Information for Business Card

I am a minimalist, but would like something to pop and stand out amongst other cards, make it memorable.

Font styles to use
Serif
Decorative
Script

```html
<!DOCTYPE html>
<html lang="en">
<head>
<meta charset="utf-8">
<title>RKP Marlow Hollow Works – Business Cards</title>
<link href="https://fonts.googleapis.com/css2?family=Open+Sans:wght@400;600;700&display=swap" rel="stylesheet">
<style>
  :root {
    --page: #ecebe8;
    --navy-dark: #1b2840;
    --navy-mid: #3a4a66;
    --navy-light: #56657e;
    --blue: #1f4a8a;
    --blue-deep: #183a70;
    --red: #e0402c;
    --red-deep: #c22f1f;
    --white: #ffffff;
    --stripe: #e6e8ec;
    --ink: #1c2a44;
    --muted: #6b7484;
  }
  * { box-sizing: border-box; margin: 0; padding: 0; }
  html, body {
    width: 1200px;
    height: 1023px;
    overflow: hidden;
    background: var(--page);
    font-family: "Open Sans", Arial, sans-serif;
  }
  .sheet {
    width: 1200px;
    height: 1023px;
    display: flex;
    align-items: center;
    justify-content: center;
    gap: 40px;
  }
  .card {
    position: relative;
    width: 340px;
    height: 340px;
    border-radius: 34px;
    overflow: hidden;
    box-shadow: 0 6px 18px rgba(20, 30, 50, 0.18);
  }

  /* Front card */
  .card--front {
    background: linear-gradient(150deg, var(--navy-light) 0%, var(--navy-mid) 45%, var(--navy-dark) 100%);
  }
  .card--front .split {
    position: absolute;
    inset: 0;
    width: 340px;
    height: 340px;
  }
  .split .web-line {
    font-family: "Open Sans", Arial, sans-serif;
    font-size: 11px;
    fill: var(--white);
    letter-spacing: 0.02em;
  }
  .front-brand {
    position: absolute;
    left: 28px;
    bottom: 92px;
    display: flex;
    align-items: center;
    gap: 10px;
  }
  .brand-dot {
    width: 16px;
    height: 16px;
    border-radius: 50%;
    background: var(--white);
    flex: none;
  }
  .brand-name {
    font-weight: 700;
    font-size: 19px;
    line-height: 1.15;
    color: var(--white);
    letter-spacing: 0.02em;
  }
  .front-slogan {
    position: absolute;
    left: 28px;
    bottom: 54px;
    font-size: 13px;
    font-weight: 600;
    color: var(--white);
    letter-spacing: 0.03em;
  }

  /* Contact card */
  .card--contact {
    background: linear-gradient(160deg, var(--blue) 0%, var(--blue-deep) 100%);
    color: var(--white);
    padding: 96px 30px 0 34px;
  }
  .contact-name {
    font-size: 21px;
    font-weight: 700;
    margin-bottom: 30px;
  }
  .contact-list { list-style: none; }
  .contact-list li {
    display: flex;
    align-items: center;
    gap: 12px;
    font-size: 12px;
    margin-bottom: 16px;
    white-space: nowrap;
  }
  .contact-list svg { width: 14px; height: 14px; flex: none; fill: var(--white); }

  /* Logo card */
  .card--logo {
    background: var(--white);
    display: flex;
    flex-direction: column;
    align-items: center;
    justify-content: center;
    gap: 18px;
    padding: 0 20px;
  }
  .logo-mark {
    display: flex;
    align-items: center;
    gap: 10px;
  }
  .logo-mark .brand-dot { background: var(--red); width: 16px; height: 16px; }
  .logo-mark .brand-name { color: var(--blue); font-size: 19px; white-space: nowrap; }
  .logo-slogan {
    font-size: 13px;
    color: var(--muted);
    letter-spacing: 0.03em;
  }
</style>
</head>
<body>
<main class="sheet">

  <section class="card card--front" aria-label="Front of card">
    <svg class="split" viewBox="0 0 340 340" aria-hidden="true">
      <defs>
        <linearGradient id="redFill" x1="0" y1="0" x2="1" y2="1">
          <stop offset="0" stop-color="#ea4a33"/>
          <stop offset="1" stop-color="#c22f1f"/>
        </linearGradient>
      </defs>
      <polygon points="168,0 196,0 340,300 340,340 322,340" fill="var(--stripe)"/>
      <polygon points="196,0 340,0 340,300" fill="url(#redFill)"/>
      <text class="web-line" x="280" y="128" text-anchor="middle" transform="rotate(64.4 280 128)">www.rkpmarlowhollowworks.net</text>
    </svg>
    <div class="front-brand">
      <span class="brand-dot"></span>
      <span class="brand-name">RKP Marlow<br>Hollow Works</span>
    </div>
    <p class="front-slogan">We offer various QVN licenses</p>
  </section>

  <section class="card card--contact" aria-label="Contact side of card">
    <h1 class="contact-name">Rowland K. Pemberly</h1>
    <ul class="contact-list">
      <li>
        <svg viewBox="0 0 24 24" aria-hidden="true"><path d="M6.6 10.8a15.2 15.2 0 0 0 6.6 6.6l2.2-2.2a1 1 0 0 1 1-.25 11.4 11.4 0 0 0 3.6.57 1 1 0 0 1 1 1V20a1 1 0 0 1-1 1A17 17 0 0 1 3 4a1 1 0 0 1 1-1h3.5a1 1 0 0 1 1 1c0 1.25.2 2.45.57 3.57a1 1 0 0 1-.25 1z"/></svg>
        555-014-2876
      </li>
      <li>
        <svg viewBox="0 0 24 24" aria-hidden="true"><path d="M2 5h20v14H2zm2 2v.5l8 5 8-5V7l-8 5z"/></svg>
        rkpmarlowhollowworks@vendrimail.com
      </li>
      <li>
        <svg viewBox="0 0 24 24" aria-hidden="true"><path d="M12 2a10 10 0 1 0 0 20 10 10 0 0 0 0-20zm0 2c.9 0 2.2 1.9 2.7 5H9.3C9.8 5.9 11.1 4 12 4zM4.3 11h3a16 16 0 0 0 .2 2h-3a8 8 0 0 1-.2-2zm.6 4h2.9c.4 1.7 1 3.1 1.8 4a8 8 0 0 1-4.7-4zm4.4 0h5.4c-.5 3.1-1.800 5-2.7 5s-2.2-1.9-2.7-5zm0-4h5.4a14 14 0 0 1 0 2H9.3a14 14 0 0 1 0-2zm7.4 0h3a8 8 0 0 1 0 2h-3a16 16 0 0 0 0-2zm-.5 4h2.9a8 8 0 0 1-4.7 4c.8-.9 1.4-2.3 1.8-4zM4.9 9a8 8 0 0 1 4.7-4C8.8 5.9 8.2 7.3 7.8 9zm11.3 0c-.4-1.7-1-3.1-1.8-4a8 8 0 0 1 4.7 4z"/></svg>
        www.rkpmarlowhollowworks.net
      </li>
    </ul>
  </section>

  <section class="card card--logo" aria-label="Logo side of card">
    <div class="logo-mark">
      <span class="brand-dot"></span>
      <span class="brand-name">RKP Marlow Hollow Works</span>
    </div>
    <p class="logo-slogan">We offer various QVN licenses</p>
  </section>

</main>
</body>
</html>
```